Coldforge Prime manufacturing Project

We are looking at getting a brand new design for a new company that deals in selling stainless tubing and other stainless still products such as handrails, Spigots, Balustrade Fittings
Glass, Glass fittings and Aluminium Channels

We require a very clean website that deals with the following colours:

Blue to light blues
Blacks
Greys to light Greys
Whites

We are open for other ideas BUT we *DO NOT* want any pinks, greens or bright colours except for backgrounds colours we have chosen above. (It can be solid, gradient or a subtle pattern)

YOU MUST KEEP THE LOGO AS IS. PLEASE DO NOT ALTER THE LOGO IN *ANY WAY* and the logo MUST be the same colours and fonts.

Logo is attached.

The site must contain these aspects:
jQuery Slider (Image slide show)
Top drop down Menus
Be no more than 900px wide
Text is to be to the w3C standards. (no special fonts)

We will chop up the design into html format. You just need to provide the PSD file.

The clients opposition is:
www.quorvatrim.example

Industry/Entity Type

It Company

Requirements
Nice to have
• Alter the logo in anyway

Files

```html
<!DOCTYPE html>
<html lang="en">
<head>
<meta charset="utf-8">
<title>Coldforge Prime – Stainless Railing &amp; Glass Systems</title>
<link rel="stylesheet" href="https://fonts.googleapis.com/css2?family=Raleway:wght@400;500;600;700&family=Roboto:wght@400;500&display=swap">
<style>
  :root{
    --blue:#1a4f8a;
    --blue-dark:#0f3f78;
    --blue-bright:#2e7fc4;
    --ink:#333;
    --text:#3a3a3a;
    --grey-bg:#e3e3e3;
    --grey-mid:#a9a9a9;
    --label:#2b2b2b;
    --white:#fff;
  }
  *{box-sizing:border-box;margin:0;padding:0}
  html,body{width:1087px;height:1200px;overflow:hidden}
  body{position:relative;background:linear-gradient(180deg,#f3f3f3 0,#e6e6e6 300px,#e2e2e2 100%);font-family:"Roboto",Arial,sans-serif;color:var(--text)}
  .topbar{position:absolute;left:0;top:0;width:100%;height:5px;background:#2d2d2d}

  .brand{position:absolute;left:112px;top:24px;width:150px;text-align:center}
  .brand-mark{width:88px;height:88px;margin:0 auto;border-radius:50%;background:var(--blue-dark)}
  .brand-name{margin-top:14px;font-family:"Raleway",sans-serif;font-weight:600;font-size:18px;color:var(--ink);white-space:nowrap}

  .search{position:absolute;left:784px;top:38px;width:200px;height:34px;border-radius:17px;background:linear-gradient(#e9e9e9,#f7f7f7);border:1px solid #cfcfcf;box-shadow:inset 0 2px 3px rgba(0,0,0,.15)}
  .search svg{position:absolute;left:10px;top:8px}

  .nav{position:absolute;left:368px;top:104px;width:624px;height:43px;border-radius:14px;background:linear-gradient(#2463a3,#154f8d);display:flex;align-items:center;justify-content:space-around;padding:0 4px}
  .nav a{color:var(--white);text-decoration:none;font-size:13px;font-family:"Roboto",sans-serif;letter-spacing:.2px;position:relative}
  .nav .sep{width:1px;height:16px;background:rgba(255,255,255,.35)}

  .hero{position:absolute;left:96px;top:172px;width:895px;height:382px;background:linear-gradient(120deg,#b87a52 0%,#8e7260 35%,#7d8486 60%,#5c6468 100%)}
  .hero-shadow{position:absolute;left:96px;top:554px;width:895px;height:18px;background:radial-gradient(ellipse at top,rgba(0,0,0,.45),rgba(0,0,0,0) 70%)}
  .hero-caption{position:absolute;left:130px;top:258px;width:427px;height:175px;background:rgba(40,40,40,.82);padding:6px 10px}
  .hero-title{font-family:"Raleway",sans-serif;font-weight:700;font-size:29px;line-height:36px;color:var(--blue-bright);white-space:nowrap;letter-spacing:-.2px}
  .hero-sub{font-family:"Raleway",sans-serif;font-weight:500;font-size:31px;line-height:38px;color:var(--white);white-space:nowrap}
  .hero-text{margin-top:8px;font-size:12.5px;line-height:18px;color:#e9e9e9;width:405px}
  .btn-learn{position:absolute;left:140px;top:407px;width:162px;height:45px;background:var(--blue-dark);color:var(--white);font-family:"Raleway",sans-serif;font-size:22px;display:flex;align-items:center;justify-content:center;gap:8px}

  .intro{position:absolute;left:96px;top:590px;width:600px}
  .intro h1{font-family:"Raleway",sans-serif;font-weight:500;font-size:33px;color:var(--ink)}
  .intro h1 span,.products h2 span{color:var(--blue)}
  .intro p{margin:16px 0 0 3px;font-size:12.5px;line-height:16.5px;color:var(--text);width:600px}
  .intro p:first-of-type{margin-top:14px}
  .btn-read{position:absolute;left:596px;top:781px;width:100px;height:27px;background:var(--blue-dark);color:var(--white);font-size:15px;display:flex;align-items:center;justify-content:center}
  .vrule{position:absolute;left:713px;top:598px;height:210px;border-left:1px dotted #888}

  .btn-catalogue{position:absolute;left:738px;top:598px;width:249px;height:38px;background:var(--blue-dark);color:var(--white);font-family:"Raleway",sans-serif;font-size:22px;display:flex;align-items:center;justify-content:center;gap:8px;border-radius:2px}
  .new-products{position:absolute;left:739px;top:644px;width:248px;height:163px;border:3px solid #3a3a3a;background:linear-gradient(180deg,#3c4750,#7e93a2 45%,#aebecb)}
  .new-products span{position:absolute;left:0;top:70px;padding:2px 8px;background:rgba(220,225,230,.35);color:var(--white);font-family:Georgia,serif;font-size:20px;letter-spacing:1px}

  .hrule{position:absolute;left:100px;top:847px;width:883px;border-top:1px dotted #8a8a8a}
  .products h2{position:absolute;left:100px;top:858px;font-family:"Raleway",sans-serif;font-weight:500;font-size:28px;color:var(--ink)}

  .arrow{position:absolute;top:970px;width:36px;height:37px;background:var(--grey-mid);display:flex;align-items:center;justify-content:center}
  .arrow.prev{left:103px}.arrow.next{left:944px}

  .product{position:absolute;top:918px;width:147px}
  .product-photo{height:137px;border:4px solid #b5b5b5}
  .product-label{margin-top:5px;height:26px;background:var(--label);color:var(--white);font-size:14px;display:flex;align-items:center;justify-content:center;letter-spacing:.2px}

  .footer{position:absolute;left:0;top:1133px;width:100%;height:67px;background:var(--blue-dark)}
  .footer-links{position:absolute;left:98px;top:13px;display:flex;gap:15px;font-size:12px;color:var(--white)}
  .footer-links a{color:var(--white);text-decoration:none}
  .copyright{position:absolute;left:97px;top:35px;font-size:12.5px;color:var(--white)}
  .social{position:absolute;left:796px;top:20px;display:flex;gap:4px}
  .social span{width:28px;height:28px;border-radius:50%;background:#f2f2f2}
</style>
</head>
<body>
  <div class="topbar"></div>

  <div class="brand">
    <div class="brand-mark"></div>
    <div class="brand-name">Coldforge Prime</div>
  </div>

  <div class="search">
    <svg width="18" height="18" viewBox="0 0 18 18"><circle cx="7" cy="7" r="5" fill="none" stroke="#333" stroke-width="2"/><line x1="11" y1="11" x2="16" y2="16" stroke="#333" stroke-width="2.5"/></svg>
  </div>

  <nav class="nav">
    <a href="#">HOME</a><span class="sep"></span>
    <a href="#">ABOUT</a><span class="sep"></span>
    <a href="#">VELMAR</a><span class="sep"></span>
    <a href="#">PRODUCTS</a><span class="sep"></span>
    <a href="#">DOWNLOAD</a><span class="sep"></span>
    <a href="#">CONTACT US</a>
  </nav>

  <div class="hero" role="img" aria-label="Stainless steel railing with glass panels beside a carpeted staircase"></div>
  <div class="hero-shadow"></div>
  <div class="hero-caption">
    <div class="hero-title">STAINLESS STEEL RAILING</div>
    <div class="hero-sub">&amp; GLASS SYSTEMS</div>
    <p class="hero-text">Lorem Ipsum has been the industry's standard dummy text ever since the 1500s, when an unknown printer took a galley</p>
  </div>
  <div class="btn-learn">Learn More
    <svg width="20" height="20" viewBox="0 0 20 20"><circle cx="10" cy="10" r="9" fill="#fff"/><path d="M6 6l4 4-4 4M10 6l4 4-4 4" fill="none" stroke="#0f3f78" stroke-width="1.8"/></svg>
  </div>

  <section class="intro">
    <h1>Coldforge <span>Prime</span></h1>
    <p>Lorem Ipsum has been the industry's standard dummy text ever since the 1500s, when an unknown printer took a galley of type and scrambled it to make a type specimen book.</p>
    <p>It has survived not only five centuries, but also the leap into electronic typesetting, remaining essentially unchanged. It was popularised in the 1960s with the release of Letraset sheets containing.</p>
    <p>Lorem Ipsum passages, and more recently with desktop publishing software like Aldus PageMaker including versions of Lorem Ipsum.</p>
  </section>
  <div class="btn-read">Read More...</div>
  <div class="vrule"></div>

  <div class="btn-catalogue">Download Catalogue
    <svg width="22" height="22" viewBox="0 0 22 22"><rect x="1" y="1" width="20" height="20" rx="2" fill="#dfe6ee"/><path d="M11 4v9M7 9l4 4 4-4" fill="none" stroke="#0f3f78" stroke-width="2.2"/><rect x="5" y="15" width="12" height="2.5" fill="#0f3f78"/></svg>
  </div>
  <div class="new-products" role="img" aria-label="Close-up of a polished stainless handrail bracket"><span>New Products</span></div>

  <div class="hrule"></div>
  <section class="products">
    <h2>Velmar <span>Products</span></h2>
    <div class="arrow prev"><svg width="12" height="16" viewBox="0 0 12 16"><path d="M10 0v16L0 8z" fill="#fff"/></svg></div>
    <div class="arrow next"><svg width="12" height="16" viewBox="0 0 12 16"><path d="M2 0v16l10-8z" fill="#fff"/></svg></div>

    <div class="product" style="left:157px"><div class="product-photo" role="img" aria-label="Railing post with glass clamp" style="background:linear-gradient(90deg,#8d9698,#b9c0c3 50%,#959ea2)"></div><div class="product-label">Railing System</div></div>
    <div class="product" style="left:312px"><div class="product-photo" role="img" aria-label="Polished stainless post on base plate" style="background:linear-gradient(90deg,#6f6a68,#c9c6c4 45%,#8b8683)"></div><div class="product-label">Railing System</div></div>
    <div class="product" style="left:468px"><div class="product-photo" role="img" aria-label="Stainless post with tensioned wire balustrade" style="background:linear-gradient(90deg,#f2f2f2,#e0e0e0 70%,#8c8c8c)"></div><div class="product-label">Post &amp; Balustrade</div></div>
    <div class="product" style="left:623px"><div class="product-photo" role="img" aria-label="Square tube fitting mounted on timber" style="background:linear-gradient(90deg,#8fa8aa,#a9bcbd 60%,#9a6e48)"></div><div class="product-label">Square tube Fittings</div></div>
    <div class="product" style="left:779px"><div class="product-photo" role="img" aria-label="Wire swaging hand tool" style="background:linear-gradient(180deg,#fafafa,#eef0f1)"></div><div class="product-label">Accessories</div></div>
  </section>

  <footer class="footer">
    <div class="footer-links">
      <a href="#">Home</a><span>|</span><a href="#">About</a><span>|</span><a href="#">Velmar</a><span>|</span><a href="#">Products</a><span>|</span><a href="#">Download</a><span>|</span><a href="#">Contact us</a>
    </div>
    <div class="copyright">Copyright © VELMAR. All Rights Reserved.</div>
    <div class="social" aria-label="Social links"><span></span><span></span><span></span><span></span><span></span><span></span></div>
  </footer>
</body>
</html>
```